Pediatric Dental Practice needs a postcard for direct mail advertising

We are looking for a creative and professional double-sided postcard design for a direct mail marketing campaign. Our goal is to attract new families to our pediatric dental practice by conveying a sense of warmth, modern care, and clinical excellence. The design should feel "boutique" and high-end yet remain fun and approachable for parents and children.

```html
<!DOCTYPE html>
<html lang="en">
<head>
<meta charset="utf-8">
<title>Maple Grove Pediatric Dentistry – Direct Mail Postcard</title>
<link href="https://fonts.googleapis.com/css2?family=Montserrat:wght@400;500;600;700&family=Allura&display=swap" rel="stylesheet">
<style>
  :root{
    --bg:#e6e6e6;
    --paper:#ffffff;
    --ink:#333336;
    --green:#2e9c55;
    --green-dark:#12683a;
    --green-light:#a8d8ae;
    --rule:#2e9c55;
    --photo-wall:#c9c8b4;
    --photo-sage:#a9bfae;
    --photo-wood:#e3c9a2;
    --photo-light:#efefea;
  }
  *{margin:0;padding:0;box-sizing:border-box}
  html,body{width:1200px;height:928px;overflow:hidden}
  body{background:var(--bg);font-family:"Montserrat",sans-serif;color:var(--ink);position:relative}

  .card{position:absolute;left:100px;width:1000px;height:340px;background:var(--paper);box-shadow:0 4px 8px rgba(60,60,110,.25);overflow:hidden}
  .card--front{top:100px}
  .card--back{top:486px}
  .abs{position:absolute}
  .center{text-align:center}

  /* brand block */
  .brand-dot{border-radius:50%;background:var(--green-light)}
  .brand-name{font-family:"Montserrat",sans-serif;font-weight:600;color:var(--ink);letter-spacing:.5px;line-height:1}
  .brand-sub{font-weight:500;letter-spacing:4px;color:var(--ink);line-height:1}

  /* front */
  .tagline{left:0;width:376px;top:160px;font-weight:700;font-size:17px;white-space:nowrap}
  .script{font-family:"Allura",cursive;font-weight:400;color:var(--green)}
  .tagline .script{font-size:30px;margin-left:6px}
  .divider{left:50px;top:196px;width:278px;height:18px}
  .intro{left:0;width:376px;top:221px;font-size:12.5px;line-height:15px}
  .features{left:40px;top:262px;width:320px;height:60px;display:flex}
  .feature{flex:1;text-align:center;font-size:7px;line-height:8.8px;text-transform:uppercase;color:#555}
  .feature + .feature{border-left:1.2px solid var(--green-light)}
  .feature svg{display:block;margin:0 auto 4px}
  .photo{left:0;top:0}

  /* back */
  .headline{left:0;width:420px;top:44px;font-size:25px;font-weight:700;line-height:31px}
  .headline .accent{color:var(--green)}
  .body-copy{left:0;width:420px;top:118px;font-size:10px;line-height:19px;font-weight:500}
  .welcome{left:0;width:420px;top:202px;font-size:28px;line-height:40px;white-space:nowrap}
  .contact-bar{left:0;top:269px;width:420px;height:41px;background:var(--green-dark);border-radius:0 16px 16px 0;color:#fff;font-size:7.4px;font-weight:500;display:flex;align-items:center;padding-left:30px;gap:22px}
  .contact-item{display:flex;align-items:center;gap:7px;line-height:10px}
  .vline{left:425px;top:57px;height:185px;border-left:1px dotted var(--green-light)}
  .address{left:444px;width:200px;top:128px;font-size:10.5px;line-height:16px}
  .promo-script{left:420px;width:250px;top:194px;font-size:31px;line-height:40px;white-space:nowrap}
  .promo-title{left:420px;width:250px;top:234px;font-size:27px;font-weight:700;letter-spacing:.3px}
  .promo-sub{left:420px;width:250px;top:274px;font-size:8.5px;font-weight:500}
  .stamp-box{left:893px;top:28px;width:78px;height:86px;border:1.3px solid #222}
  .mail-line{left:682px;width:212px;border-top:1.3px solid #222}
</style>
</head>
<body>

<!-- FRONT -->
<section class="card card--front">
  <svg class="abs photo" width="1000" height="340" viewBox="0 0 1000 340" role="img" aria-label="Photograph of the practice reception: light wood front desk, sage feature wall with practice name, green pendant lamps and potted plants">
    <defs>
      <linearGradient id="room" x1="0" y1="0" x2="0" y2="1">
        <stop offset="0" stop-color="var(--photo-light)"/>
        <stop offset=".45" stop-color="var(--photo-wall)"/>
        <stop offset=".65" stop-color="var(--photo-wood)"/>
        <stop offset="1" stop-color="var(--photo-light)"/>
      </linearGradient>
    </defs>
    <path d="M412 0 C352 60 352 150 387 210 C412 255 417 300 410 340 L1000 340 L1000 0 Z" fill="var(--green)"/>
    <path d="M418 0 C358 60 358 150 393 210 C418 255 423 300 416 340 L1000 340 L1000 0 Z" fill="var(--green-light)"/>
    <path d="M424 0 C364 60 364 150 399 210 C424 255 429 300 422 340 L1000 340 L1000 0 Z" fill="url(#room)"/>
  </svg>

  <div class="abs brand-dot" style="left:165px;top:18px;width:46px;height:46px"></div>
  <div class="abs center brand-name" style="left:0;width:376px;top:102px;font-size:32px">maple grove</div>
  <div class="abs center brand-sub" style="left:0;width:380px;top:138px;font-size:11px">PEDIATRIC DENTISTRY</div>

  <div class="abs center tagline">Healthy Smiles.<span class="script">Happy Kids.</span></div>

  <svg class="abs divider" viewBox="0 0 278 18">
    <line x1="0" y1="8" x2="120" y2="8" stroke="var(--rule)" stroke-width="1.3"/>
    <line x1="158" y1="8" x2="278" y2="8" stroke="var(--rule)" stroke-width="1.3"/>
    <path d="M139 18 L127 6 A5.5 5.5 0 0 1 139 2 A5.5 5.5 0 0 1 151 6 Z" fill="var(--green)"/>
  </svg>

  <p class="abs center intro">Compassionate care in a modern,<br>kid-friendly environment.</p>

  <div class="abs features">
    <div class="feature">
      <svg width="26" height="26" viewBox="0 0 26 26" fill="none" stroke="var(--green)" stroke-width="1.5"><path d="M13 22 L4 13 A5 5 0 0 1 13 6 A5 5 0 0 1 22 13 Z"/></svg>
      Gentle,<br>Kid-Focused<br>Care
    </div>
    <div class="feature">
      <svg width="26" height="26" viewBox="0 0 26 26" fill="none" stroke="var(--green)" stroke-width="1.5"><path d="M13 2 L22 5 V12 C22 18 18 22 13 24 C8 22 4 18 4 12 V5 Z"/><path d="M9 13 L12 16 L17 10"/></svg>
      Preventive<br>&amp; Restorative<br>Dentistry
    </div>
    <div class="feature">
      <svg width="26" height="26" viewBox="0 0 26 26" fill="none" stroke="var(--green)" stroke-width="1.5"><circle cx="13" cy="13" r="11"/><path d="M8 13 L11.5 16.5 L18 10"/></svg>
      Comfortable,<br>Modern<br>Environment
    </div>
    <div class="feature">
      <svg width="40" height="26" viewBox="0 0 40 26" fill="none" stroke="var(--green)" stroke-width="1.5"><circle cx="9" cy="12" r="5"/><circle cx="20" cy="9" r="6"/><circle cx="31" cy="12" r="5"/><line x1="2" y1="23" x2="38" y2="23"/></svg>
      Built on Trust,<br>Focused on<br>Families
    </div>
  </div>
</section>

<!-- BACK -->
<section class="card card--back">
  <h1 class="abs center headline"><span class="accent">Your child’s smile</span><br>is our greatest priority.</h1>
  <p class="abs center body-copy">At Maple Grove Pediatric Dentistry, we combine advanced<br>technology with a gentle touch to make every visit<br>a positive experience for kids and parents.</p>
  <p class="abs center script welcome">We can’t wait to meet your family!</p>

  <div class="abs contact-bar">
    <div class="contact-item">
      <svg width="13" height="15" viewBox="0 0 13 15"><path d="M6.5 15 C2 9.5 0 7.5 0 5.5 A6.5 6 0 0 1 13 5.5 C13 7.5 11 9.5 6.5 15 Z" fill="#fff"/><circle cx="6.5" cy="5.5" r="2.2" fill="var(--green-dark)"/></svg>
      <span class="center">48 Meadow Lane, Suite 200<br>Fairbrook, CT 06500</span>
    </div>
    <div class="contact-item" style="margin-left:4px">
      <svg width="11" height="11" viewBox="0 0 24 24"><path fill="#fff" d="M6.6 10.8a15.1 15.1 0 0 0 6.6 6.6l2.2-2.2a1 1 0 0 1 1-.25 11.4 11.4 0 0 0 3.6.6 1 1 0 0 1 1 1V20a1 1 0 0 1-1 1A17 17 0 0 1 3 4a1 1 0 0 1 1-1h3.5a1 1 0 0 1 1 1c0 1.250.2 2.45.6 3.6a1 1 0 0 1-.25 1z"/></svg>
      <span>(203) 555-0142</span>
    </div>
    <div class="contact-item">
      <svg width="12" height="12" viewBox="0 0 24 24" fill="none" stroke="#fff" stroke-width="1.8"><circle cx="12" cy="12" r="10"/><ellipse cx="12" cy="12" rx="4.5" ry="10"/><line x1="2" y1="12" x2="22" y2="12"/><line x1="4" y1="7" x2="20" y2="7"/><line x1="4" y1="17" x2="20" y2="17"/></svg>
      <span>maplegrovedentistry.com</span>
    </div>
  </div>

  <div class="abs vline"></div>

  <div class="abs brand-dot" style="left:522px;top:22px;width:46px;height:46px"></div>
  <div class="abs center brand-name" style="left:444px;width:200px;top:84px;font-size:26px">maple grove</div>
  <div class="abs center brand-sub" style="left:444px;width:204px;top:112px;font-size:9px;letter-spacing:3.2px">PEDIATRIC DENTISTRY</div>
  <p class="abs center address">48 Meadow Lane, Suite 200<br>Fairbrook, CT 06500</p>

  <p class="abs center script promo-script">A Healthy Smile</p>
  <p class="abs center promo-title">STARTS HERE</p>
  <p class="abs center promo-sub">Expert care. Kind hearts. Bright futures.</p>

  <div class="abs stamp-box"></div>
  <div class="abs mail-line" style="top:178px"></div>
  <div class="abs mail-line" style="top:213px"></div>
  <div class="abs mail-line" style="top:243px"></div>
  <div class="abs mail-line" style="top:273px"></div>
</section>

</body>
</html>
```